Flyer-Design für Betreuung von pflegebedürftigen/hilfebedürftigen Senioren
Ich bin begeistert! Sehr gute und geduldige Bearbeitung meiner Änderungswünsche. Gute und schnelle Kommunikation. Danke!
Zielgruppe
Alltagshilfe, Betreuung, Begleitung und Unterstützung von pflegebedürftigen/hilfebedürftigen Senioren
Wir begleiten Senioren im Alltag, in Ihrer Freizeit, zu Ausflügen und Veranstaltungen, oder einfach mal zum Kaffee trinken. Wir erledigen Einkäufe, unterstützen bei Arzt und Behördengängen oder haben einfach nur ein offenes Ohr und schenken unsere Zeit. Gesellschaftsspiele, Gedächtnistraining und Erinnerungspflege für die kognitive Aktivierung kommen unter anderem bei den betreuen Demenzkranken zum Einsatz. Auch die physische Aktivierung in Form von Spaziergängen oder Bewegungsübungen gehört zum Arbeitsalltag.
Wir betreuuen die Senioren stundenweise im eigenen häuslichen Umfeld. Dadurch werden deren pflegende Angehörige entlastet und der Senior dabei unterstützt, seine Eigenständigkeit zu erhalten.
Aufgabenstellung
Nach Möglichkeit hätte ich gern Bilder eingebunden, auf denen keine Menschen sondern eher Figuren zu sehen sind, welche Liebe, Zusammenhalt, Familie und Unterstützung suggerieren, ähnlich wie bei dem Beispielflyer den ich mit hochlade. Die Schrift sollte Seniorengerecht und evtl. in Anlehnung an das Logo sein (Lindauer Altenbeistand - Helvetica Neue - 43 Light Extended / Slogan - Lato - Bold ). Die Farben des Logos, welche sich gern im Flyer wiederfinden dürfen sind: Rot: #BA2428 ; Orange: #F26C21
Vielleicht könnte man Puzzleteile kreativ einarbeiten? Senioren- und Alltagsbegleitung im häuslichen Umfeld ist ja einer von mehreren Bausteinen (neben Pflegedienst ect) der die Angehörigen entlastet und die Senioren unterstützt um den Alltag solange wie möglich in den eigenen 4 Wänden zu organisieren.. Allerdings kein Muss, nur ein Gedanke.
Auch bezüglich des Textes bin ich noch nicht 100% sicher. Gibt es die Möglichkeit, ein Vorgesehenes Textfeld nach dem Erwerb des Designs selbst zu ändern? Am besten mit Microsoft Word, oder so?

```html
<!DOCTYPE html>
<html lang="de">
<head>
<meta charset="utf-8">
<title>Lindauer Altenbeistand – Flyer</title>
<link href="https://fonts.googleapis.com/css2?family=Lato:wght@400;700;900&display=swap" rel="stylesheet">
<style>
  :root {
    --red: #ba2428;
    --red-deep: #a3171f;
    --orange: #e0600f;
    --orange-light: #f26c21;
    --paper: #f7f7f6;
    --stage: #e2e3e5;
    --ink: #4a4a4a;
    --white: #ffffff;
  }
  * { margin: 0; padding: 0; box-sizing: border-box; }
  html, body { width: 1200px; height: 2400px; overflow: hidden; }
  body { background: var(--stage); font-family: "Lato", sans-serif; position: relative; }

  .flyer-page {
    position: absolute; left: 355px; width: 490px; height: 1047px;
    background: var(--paper); overflow: hidden;
  }
  .flyer-page--front { top: 90px; }
  .flyer-page--back { top: 1228px; }
  .page-bands { position: absolute; inset: 0; width: 490px; height: 1047px; }

  /* front */
  .brand { position: absolute; left: 0; right: 0; top: 80px; text-align: center; }
  .brand-line { display: flex; align-items: center; justify-content: center; gap: 12px; }
  .brand-dot { width: 34px; height: 34px; border-radius: 50%; background: var(--orange-light); }
  .brand-name { font-size: 34px; font-weight: 400; color: var(--red); line-height: 1.05; text-align: left; }
  .brand-owner { margin-top: 14px; font-size: 20px; font-weight: 700; color: var(--orange-light); }
  .brand-slogan { margin-top: 12px; font-size: 12.5px; font-weight: 700; letter-spacing: 2.6px; color: var(--red); }

  .service-wheel { position: absolute; left: 0; top: 0; width: 490px; height: 1047px; }

  .front-headline {
    position: absolute; left: 0; right: 0; top: 846px; text-align: center;
    color: var(--white); font-weight: 900; font-size: 40px; line-height: 46px;
  }
  .front-url {
    position: absolute; left: 0; right: 0; top: 993px; text-align: center;
    color: var(--white); font-weight: 700; font-size: 19px;
  }

  /* back */
  .services-title {
    position: absolute; left: 33px; top: 70px; font-size: 48px; font-weight: 900;
    background: linear-gradient(90deg, var(--red-deep), var(--orange) 70%, var(--red));
    -webkit-background-clip: text; background-clip: text; color: transparent;
  }
  .services-list { position: absolute; left: 32px; top: 160px; width: 430px; list-style: none; }
  .services-list li {
    position: relative; padding-left: 40px; font-size: 20.5px; line-height: 25.5px;
    color: var(--ink); margin-bottom: 12px;
  }
  .services-list .tick { position: absolute; left: 0; top: 4px; width: 22px; height: 22px; }
  .cost-note {
    position: absolute; left: 71px; top: 810px; font-size: 13px; line-height: 16px;
    font-weight: 700; color: #555;
  }
  .contact { position: absolute; left: 0; right: 0; top: 900px; text-align: center; color: var(--white); font-weight: 700; font-size: 18.5px; }
  .contact p { line-height: 32.5px; }
  .contact .contact-name { text-decoration: underline; text-underline-offset: 3px; }
</style>
</head>
<body>

<section class="flyer-page flyer-page--front">
  <svg class="page-bands" viewBox="0 0 490 1047" aria-hidden="true">
    <defs>
      <linearGradient id="bandFront" x1="0" x2="1" y1="0" y2="0">
        <stop offset="0" stop-color="#a3171f"/>
        <stop offset="0.5" stop-color="#e0600f"/>
        <stop offset="1" stop-color="#a3171f"/>
      </linearGradient>
    </defs>
    <path d="M0,0 H490 V30 C330,28 70,22 0,66 Z" fill="url(#bandFront)"/>
    <path d="M0,822 C230,830 430,800 490,698 V1047 H0 Z" fill="url(#bandFront)"/>
  </svg>

  <header class="brand">
    <div class="brand-line">
      <span class="brand-dot"></span>
      <span class="brand-name">Lindauer<br>Altenbeistand</span>
    </div>
    <p class="brand-owner">Inh. Hanna Folmerit</p>
    <p class="brand-slogan">BEGLEITUNG-BETREUUNG-WERTSCHÄTZUNG</p>
  </header>

  <svg class="service-wheel" viewBox="0 0 490 1047">
    <defs>
      <radialGradient id="photoTone" cx="0.5" cy="0.45" r="0.6">
        <stop offset="0" stop-color="#d9a48a"/>
        <stop offset="0.55" stop-color="#b3a27a"/>
        <stop offset="1" stop-color="#6f8a4a"/>
      </radialGradient>
    </defs>
    <g stroke="#e0600f" stroke-width="1.3" stroke-dasharray="2 3">
      <line x1="243" y1="374" x2="243" y2="350"/>
      <line x1="243" y1="654" x2="243" y2="678"/>
      <line x1="103" y1="514" x2="79" y2="514"/>
      <line x1="383" y1="514" x2="407" y2="514"/>
      <line x1="144" y1="415" x2="127" y2="398"/>
      <line x1="342" y1="415" x2="359" y2="398"/>
      <line x1="144" y1="613" x2="127" y2="630"/>
      <line x1="342" y1="613" x2="359" y2="630"/>
    </g>
    <circle cx="243" cy="514" r="133" fill="none" stroke="#e0600f" stroke-width="2"/>
    <circle cx="243" cy="514" r="125" fill="url(#photoTone)" role="img" aria-label="Foto: eine ältere Hand ruht in einer jüngeren Hand"/>
    <g fill="#e8672a">
      <circle cx="243" cy="323" r="20" role="img" aria-label="Symbol Schaukelstuhl"/>
      <circle cx="376" cy="376" r="20" role="img" aria-label="Symbol Wollknäuel"/>
      <circle cx="434" cy="514" r="20" role="img" aria-label="Symbol Brille"/>
      <circle cx="376" cy="652" r="20" role="img" aria-label="Symbol Telefon"/>
      <circle cx="243" cy="705" r="20" role="img" aria-label="Symbol Baum"/>
      <circle cx="110" cy="652" r="20" role="img" aria-label="Symbol Wohnhaus"/>
      <circle cx="52" cy="514" r="20" role="img" aria-label="Symbol älteres Paar mit Gehstöcken"/>
      <circle cx="110" cy="376" r="20" role="img" aria-label="Symbol Rollstuhl"/>
    </g>
  </svg>

  <h1 class="front-headline">Dienstleistungen<br>für Senioren und den<br>Alltag in Dresden</h1>
  <p class="front-url">www.lindauer-altenbeistand.de</p>
</section>

<section class="flyer-page flyer-page--back">
  <svg class="page-bands" viewBox="0 0 490 1047" aria-hidden="true">
    <defs>
      <linearGradient id="bandBack" x1="0" x2="1" y1="0" y2="0">
        <stop offset="0" stop-color="#a3171f"/>
        <stop offset="0.5" stop-color="#e0600f"/>
        <stop offset="1" stop-color="#a3171f"/>
      </linearGradient>
    </defs>
    <path d="M0,0 H490 V30 C330,28 70,22 0,82 Z" fill="url(#bandBack)"/>
    <path d="M0,876 C230,882 430,850 490,752 V1047 H0 Z" fill="url(#bandBack)"/>
  </svg>

  <h2 class="services-title">Unsere Leistungen</h2>

  <ul class="services-list">
    <li><svg class="tick" viewBox="0 0 22 22"><path d="M2,12 L8,19 L20,2" fill="none" stroke="#c0281f" stroke-width="3.2" stroke-linecap="round" stroke-linejoin="round"/></svg>Unterstützung bei der Alltagsgestaltung</li>
    <li><svg class="tick" viewBox="0 0 22 22"><path d="M2,12 L8,19 L20,2" fill="none" stroke="#c0281f" stroke-width="3.2" stroke-linecap="round" stroke-linejoin="round"/></svg>Demenzbetreuung</li>
    <li><svg class="tick" viewBox="0 0 22 22"><path d="M2,12 L8,19 L20,2" fill="none" stroke="#c0281f" stroke-width="3.2" stroke-linecap="round" stroke-linejoin="round"/></svg>Körperliche Aktivierung<br>(Spaziergänge, Spiele, etc.)</li>
    <li><svg class="tick" viewBox="0 0 22 22"><path d="M2,12 L8,19 L20,2" fill="none" stroke="#c0281f" stroke-width="3.2" stroke-linecap="round" stroke-linejoin="round"/></svg>Erinnerungspflege/Biographiearbeit/<br>Gedächtnistraining</li>
    <li><svg class="tick" viewBox="0 0 22 22"><path d="M2,12 L8,19 L20,2" fill="none" stroke="#c0281f" stroke-width="3.2" stroke-linecap="round" stroke-linejoin="round"/></svg>Gespräche über Aktuelles und<br>Vergangenes</li>
    <li><svg class="tick" viewBox="0 0 22 22"><path d="M2,12 L8,19 L20,2" fill="none" stroke="#c0281f" stroke-width="3.2" stroke-linecap="round" stroke-linejoin="round"/></svg>Begleitung zu außerhäuslichen Terminen<br>(Ärzte, Behörden, etc.)</li>
    <li><svg class="tick" viewBox="0 0 22 22"><path d="M2,12 L8,19 L20,2" fill="none" stroke="#c0281f" stroke-width="3.2" stroke-linecap="round" stroke-linejoin="round"/></svg>Organisation von weiteren<br>Unterstützungsangeboten</li>
    <li><svg class="tick" viewBox="0 0 22 22"><path d="M2,12 L8,19 L20,2" fill="none" stroke="#c0281f" stroke-width="3.2" stroke-linecap="round" stroke-linejoin="round"/></svg>Hauswirtschaftliche Unterstützung/<br>Gartenpflege</li>
    <li><svg class="tick" viewBox="0 0 22 22"><path d="M2,12 L8,19 L20,2" fill="none" stroke="#c0281f" stroke-width="3.2" stroke-linecap="round" stroke-linejoin="round"/></svg>Gemeinsame Unternehmungen<br>(Museum, Theater, etc.)</li>
    <li><svg class="tick" viewBox="0 0 22 22"><path d="M2,12 L8,19 L20,2" fill="none" stroke="#c0281f" stroke-width="3.2" stroke-linecap="round" stroke-linejoin="round"/></svg>Individuelle Ausflüge (Zoo, Kino,<br>Restaurant...)</li>
    <li><svg class="tick" viewBox="0 0 22 22"><path d="M2,12 L8,19 L20,2" fill="none" stroke="#c0281f" stroke-width="3.2" stroke-linecap="round" stroke-linejoin="round"/></svg>Gesellschaft leisten und Zeit schenken</li>
  </ul>

  <p class="cost-note">Die Kostenübernahme ist bei bestehendem<br>Pflegegrad durch die Pflegekasse möglich.</p>

  <address class="contact">
    <p class="contact-name">Lindauer Altenbeistand Hanna Folmerit</p>
    <p>Lindenweg 14 · 01234 Dresden</p>
    <p>Tel.: 0170 55 18 204</p>
    <p>info@lindauer-altenbeistand.de</p>
  </address>
</section>

</body>
</html>
```